Affiliate website design and wireframe

We need a design of an affiliate website for an application we purchased, it is important that you build the website pages according to the developer of the applications specifications (please see attached documents) the developer of the application will configure the pages and add them to the site. Please take special note of his comments below.

We all so need you to create a wire frame so the developer can test everything (http://quartz.lomeriva.vn/)

It will be the homepage and about 16 inner pages (please see attached files)
Here is our website http://maplecourtlink.com/affiliate/affiliates/index.php

The version of the software we purchased is the Quill Partner Grid version

Comments from the developers

1. I will need the source files of the design (photoshop .psd files and font files if custom fonts are used), since the implementation is closely bound to component sizes (like border width, margin width etc.) and colors. If you own a corporate design manual, it's crucial to send it as well. Also, please, make sure if you use custom fonts, that these allow legal website integration (like zorvix web fonts).

2. Any and every content is controlled via templates. All editing/adding/removing etc. is done here. The template files are essentially html/php documents, they use a template engine called brisko (http://www.brisko.net/) which has it's own language similar to php.

3. .psd files are ideal, because we deal with the specifics of QPS/QPG implementation on a daily basis. Any html/css developed in advance may prove to be a poor choice. You may choose to let an in-house developer do the job, but experience wise this is more costly, since he will not be accustomed to the template/functionality systems of QPS/QPG.

4. I will need the source files of the design (photoshop .psd files and font files if custom fonts are used), since the implementation is closely bound to component sizes (like border width, margin width etc.) and colors. If you own a corporate design manual, it's crucial to send it as well. Also, please, make sure if you use custom fonts, that these allow legal website integration (like zorvix web fonts).

Regards,

Tomas Vereck

We prefer illustrations more than pictures of real people.

This is the home page, it is asking for Merchant and Affiliate sign up, not just affiliate.

http://maplecourtlink.com/affiliate/index.php

Please note the home page features both Merchant and Affiliate sign up

We are looking for illustration design not just stock images

Please remember the search menu that searches for the available programs, see the example we gave you, look at the search menu at the top of the page http://www.tradolink.com/

We are reviewing everything, no need to send more designs

Target Market(s)

Natural Products Manufacturers
Natural products Sales reps
Natural Products Bloggers
Social Marketing

Industry/Entity Type

Software

Requirements
Must have
• 1. All links on pages should go to the appropriate pages.
2. Colors can be based on our logo design (look at the attachments)
3. Here is our website http://maplecourtlink.com/affiliate/affiliates/index.php
4. We have attached a drawing of how we think the homepage concept should follow.
5. Main concept of design, is trying to show our sales people (Affiliates) are doing multiple things to advertise and sell the merchants products.(see logo)
6. Need to be able to edit all text and images.
7. Our target audience is Natural product sales people (Advertisers, bloggers, ext) and natural product manufacturers.
8. You can speak to the company who made the application, through live chat, on there website http://www.quillpartnergrid.com/
Nice to have
• See Attached Documents.
site should take up whole website pages
Look For fun Illustrated Website, one of the better ones we have seen is http://www.tradolink.com/index.cfm
Should not have
• Please look very carefully at developers comment above.

```html
<!DOCTYPE html>
<html lang="en">
<head>
<meta charset="utf-8">
<title>Maple Court Link – Affiliate Network</title>
<link href="https://fonts.googleapis.com/css2?family=Lato:wght@300;400;700&family=Open+Sans:wght@400;600;700&display=swap" rel="stylesheet">
<style>
:root{
  --navy:#1d3e72;
  --navy-dark:#163260;
  --green:#6ba51c;
  --green-light:#7fb628;
  --grey-band:#dcdcdc;
  --hero-top:#e6e6e6;
  --hero-bottom:#8e8e8e;
  --ink:#444;
  --muted:#777;
  --footer:#1b1b1b;
  --white:#fff;
}
*{margin:0;padding:0;box-sizing:border-box}
html,body{width:1200px;height:2835px;overflow:hidden}
body{position:relative;font-family:"Open Sans",Arial,sans-serif;color:var(--ink);background:var(--white)}
.abs{position:absolute}
a{color:inherit;text-decoration:none}

/* header */
.topbar{left:0;top:0;width:1200px;height:78px;background:var(--white)}
.brand{left:170px;top:0;width:275px;height:134px;background:var(--white);display:flex;align-items:center;justify-content:center;gap:10px;z-index:3}
.brand-mark{width:22px;height:22px;border-radius:50%;background:var(--green)}
.brand-name{font-family:"Lato",sans-serif;font-weight:700;font-size:24px;color:var(--navy)}
.login{top:17px;height:17px;font-size:10px;font-weight:700;color:var(--white);display:flex;align-items:center;justify-content:center}
.login.aff{left:813px;width:94px;background:var(--navy)}
.login.mer{left:915px;width:102px;background:var(--green)}
.toplink{top:48px;font-size:11px;font-weight:600;color:var(--navy)}
.mainnav{left:0;top:78px;width:1200px;height:56px;background:var(--navy)}
.nav-item{top:94px;color:var(--white);font-size:13px;font-weight:700;line-height:1}
.nav-item small{display:block;font-size:8px;font-weight:400;opacity:.8;margin-top:3px}

/* hero */
.hero{left:0;top:134px;width:1200px;height:328px;background:linear-gradient(#e8e8e8 0%,#cfcfcf 70%,#8d8d8d 70.5%,#7a7a7a 100%)}
.hero-art{left:539px;top:151px;width:463px;height:311px;background:linear-gradient(#d8dfe8,#9fb0c4);border-radius:4px}
.btn{display:flex;align-items:center;justify-content:center;font-size:12px;color:var(--white)}
.btn-aff{left:234px;top:225px;width:135px;height:28px;background:var(--green)}
.btn-mer{left:378px;top:225px;width:134px;height:28px;background:var(--navy)}
.hero-title{left:232px;top:275px;font-family:"Lato",sans-serif;font-weight:300;font-size:40px;line-height:40px;color:var(--white)}
.btn-start{left:234px;top:384px;width:135px;height:28px;background:var(--green)}
.hero-arrow{top:280px}
.hero-dots{left:594px;top:447px;display:flex;gap:6px}
.hero-dots span{width:6px;height:6px;border-radius:50%;background:var(--white);opacity:.7}

/* programs */
.programs{left:0;top:462px;width:1200px;height:278px;background:var(--navy)}
.pointer{left:566px;top:740px}
.prog-title{top:488px;font-family:"Lato",sans-serif;font-weight:400;font-size:32px;color:var(--white)}
.badge{width:94px;height:94px}
.prog-list{font-size:13px;color:var(--white);line-height:22px}
.prog-row{display:flex;align-items:center}
.prog-row .dots{flex:1;border-bottom:2px dotted rgba(255,255,255,.7);margin:0 8px;height:0;position:relative;top:2px}
.prog-row .ico{width:12px;height:12px;border-radius:50%;background:var(--green-light)}
.learn{width:106px;height:28px;background:var(--green);font-size:11px;gap:6px}

/* channels */
.section-title{left:0;width:1200px;text-align:center;font-family:"Lato",sans-serif;font-weight:300;font-size:33px;color:#555}
.card{width:251px;height:165px;background:var(--green);color:var(--white);text-align:center}
.card h3{position:absolute;left:0;right:0;top:80px;font-size:12px;font-weight:700;letter-spacing:.5px}
.card p{position:absolute;left:30px;right:30px;top:105px;font-size:10px;line-height:14px;opacity:.9}
.card-badge{position:absolute;left:80px;top:-35px;width:92px;height:92px}

/* partners */
.partners{left:0;top:1351px;width:1200px;height:473px;background:repeating-linear-gradient(45deg,#dedede 0 2px,#d6d6d6 2px 4px)}
.pbox{width:184px;height:87px;background:var(--white);box-shadow:0 1px 3px rgba(0,0,0,.15);display:flex;align-items:center;justify-content:center;font-family:"Lato",sans-serif;font-weight:700;font-size:20px;color:#3c3c3c}
.carousel-arrow{width:20px;height:36px}

/* testimonials */
.testimonial{left:197px;top:1943px;width:395px;height:351px;background:var(--white);box-shadow:0 0 4px rgba(0,0,0,.18)}
.quote-mark{font-family:Georgia,serif;font-size:40px;color:#444;line-height:1}
.t-text{font-size:10.5px;line-height:16px;color:#555}
.t-text .more{color:var(--green);text-decoration:underline}
.t-photo{left:298px;top:53px;width:68px;height:64px;background:linear-gradient(#cfd4da,#8c97a3)}
.t-name{font-size:14px;font-weight:700;color:var(--green)}
.t-role{font-size:11px;color:#666}
.t-deco{right:30px;bottom:-45px;font-family:Georgia,serif;font-size:150px;color:#e8e8e8;line-height:1}
.client{background:var(--white);box-shadow:0 0 4px rgba(0,0,0,.18);display:flex;align-items:center;justify-content:center;text-align:center;font-family:"Lato",sans-serif;font-weight:700;color:#3b3b3b;padding:4px}
.t-dots{left:370px;top:2315px;display:flex;gap:8px}
.t-dots span{width:10px;height:10px;border-radius:50%;background:#999}
.t-dots span:first-child{background:var(--green)}

/* footer */
.footer{left:0;top:2378px;width:1200px;height:457px;background:linear-gradient(#2a2a2a,#0f0f0f)}
.f-head{font-size:15px;color:#ddd;padding-bottom:10px;border-bottom:1px solid #555}
.f-text{font-size:10px;line-height:18px;color:#bbb}
.f-links{font-size:10px;line-height:17px;color:#888}
.f-phone{font-size:22px;color:var(--white);letter-spacing:1px}
.f-mail{font-size:14px;color:#ddd}
.f-note{left:718px;top:2514px;width:248px;height:113px;background:var(--green);color:var(--white);font-size:10.5px;line-height:15px;padding:12px 16px}
.social{width:48px;height:48px;border-radius:50%;background:#555;border:2px solid #777;color:#eee;font-size:10px;display:flex;align-items:center;justify-content:center}
.f-brand{left:183px;top:2750px;font-family:"Lato",sans-serif;font-weight:700;font-size:17px;color:var(--white);display:flex;align-items:center;gap:8px}
.f-brand i{width:14px;height:14px;border-radius:50%;background:var(--green);display:block}
.copyright{left:777px;top:2780px;font-size:10px;color:#ccc}
</style>
</head>
<body>

<!-- header -->
<div class="abs topbar"></div>
<div class="abs mainnav"></div>
<a class="abs brand" href="#"><span class="brand-mark"></span><span class="brand-name">Maple Court Link</span></a>
<a class="abs login aff" href="#">AFFILIATE LOGIN</a>
<a class="abs login mer" href="#">MERCHANT LOGIN</a>
<a class="abs toplink" style="left:539px" href="#">WHAT IS AFFILIATE MARKETING?</a>
<a class="abs toplink" style="left:747px" href="#">MERCHANTS JOIN HERE</a>
<a class="abs toplink" style="left:907px" href="#">AFFILIATE SIGN UP</a>
<a class="abs nav-item" style="left:482px" href="#">POPULAR<small>Merchants</small></a>
<a class="abs nav-item" style="left:575px" href="#">HOME&amp;GARDEN<small>Merchants</small></a>
<a class="abs nav-item" style="left:709px" href="#">FASHION<small>Merchants</small></a>
<a class="abs nav-item" style="left:798px" href="#">GREEN<small>Merchants</small></a>
<a class="abs nav-item" style="left:874px" href="#">BUSINESS<small>Merchants</small></a>
<a class="abs nav-item" style="left:970px" href="#">MORE<small>Merchants</small></a>

<!-- hero -->
<section class="abs hero"></section>
<div class="abs hero-art" role="img" aria-label="Illustration of an affiliate working at a desk computer with speech bubbles showing sale, shopping, money and card icons"></div>
<a class="abs btn btn-aff" href="#">Affiliates Signup</a>
<a class="abs btn btn-mer" href="#">Merchants Signup</a>
<h1 class="abs hero-title">Make Money<br>Make Sense.</h1>
<a class="abs btn btn-start" href="#">GET STARTED</a>
<svg class="abs hero-arrow" style="left:180px" width="22" height="36" viewBox="0 0 22 36"><path d="M18 3 5 18l13 15" fill="none" stroke="#1d3e72" stroke-width="5"/></svg>
<svg class="abs hero-arrow" style="left:1005px" width="22" height="36" viewBox="0 0 22 36"><path d="M4 3l13 15L4 33" fill="none" stroke="#1d3e72" stroke-width="5"/></svg>
<div class="abs hero-dots"><span></span><span></span><span></span></div>

<!-- programs -->
<section class="abs programs"></section>
<svg class="abs pointer" width="68" height="36" viewBox="0 0 68 36"><path d="M0 0h68L34 36z" fill="#1d3e72"/></svg>

<h2 class="abs prog-title" style="left:300px">Affiliates</h2>
<svg class="abs badge" style="left:182px;top:554px" viewBox="0 0 94 94"><circle cx="47" cy="47" r="46" fill="#6ba51c"/><circle cx="47" cy="47" r="36" fill="none" stroke="#fff" stroke-width="2"/><g fill="#fff"><rect x="32" y="50" width="6" height="12"/><rect x="41" y="44" width="6" height="18"/><rect x="50" y="38" width="6" height="24"/></g><path d="M28 64h38" stroke="#fff" stroke-width="2"/></svg>
<div class="abs prog-list" style="left:299px;top:556px;width:140px">
  <div class="prog-row">Automotive<span class="dots"></span><span class="ico"></span></div>
  <div class="prog-row">Business<span class="dots"></span><span class="ico"></span></div>
  <div class="prog-row">Careers<span class="dots"></span><span class="ico"></span></div>
  <div class="prog-row">Education<span class="dots"></span><span class="ico"></span></div>
</div>
<div class="abs prog-list" style="left:465px;top:556px;width:124px">
  <div class="prog-row">Clothing<span class="dots"></span><span class="ico"></span></div>
  <div class="prog-row">Auction<span class="dots"></span><span class="ico"></span></div>
  <div class="prog-row">Media<span class="dots"></span><span class="ico"></span></div>
  <div class="prog-row">Health<span class="dots"></span><span class="ico"></span></div>
</div>
<a class="abs btn learn" style="left:299px;top:667px" href="#">Learn More</a>

<h2 class="abs prog-title" style="left:760px">Merchants</h2>
<svg class="abs badge" style="left:645px;top:554px" viewBox="0 0 94 94"><circle cx="47" cy="47" r="46" fill="#6ba51c"/><circle cx="47" cy="47" r="36" fill="none" stroke="#fff" stroke-width="2"/><g fill="#fff"><rect x="32" y="48" width="6" height="14"/><rect x="41" y="40" width="6" height="22"/><rect x="50" y="46" width="6" height="16"/></g><path d="M28 64h38" stroke="#fff" stroke-width="2"/></svg>
<div class="abs prog-list" style="left:760px;top:556px;width:258px">
  <div class="prog-row">Affiliate Diagnostics<span class="dots"></span><span class="ico"></span></div>
  <div class="prog-row">Merchant Recommendations<span class="dots"></span><span class="ico"></span></div>
  <div class="prog-row">Continuing Education<span class="dots"></span><span class="ico"></span></div>
  <div class="prog-row">Training Webinars<span class="dots"></span><span class="ico"></span></div>
</div>
<a class="abs btn learn" style="left:760px;top:667px" href="#">Learn More</a>

<!-- channels -->
<h2 class="abs section-title" style="top:802px">We Leave the Marketing Decisions to You</h2>

<div class="abs card" style="left:197px;top:900px">
  <svg class="card-badge" viewBox="0 0 92 92"><circle cx="46" cy="46" r="44" fill="#fff" stroke="#6ba51c" stroke-width="2" stroke-dasharray="4 3"/><circle cx="46" cy="46" r="36" fill="#fff" stroke="#ccc"/><g fill="#6ba51c"><circle cx="56" cy="34" r="6"/><circle cx="36" cy="46" r="6"/><circle cx="56" cy="58" r="6"/></g><path d="M56 34 36 46l20 12" stroke="#6ba51c" stroke-width="3" fill="none"/></svg>
  <h3>SOCIAL NETWORKS</h3><p>Lorem Ipsum is simply dummy text of the printing and typesetting industry.</p>
</div>
<div class="abs card" style="left:474px;top:900px">
  <svg class="card-badge" viewBox="0 0 92 92"><circle cx="46" cy="46" r="44" fill="#fff" stroke="#6ba51c" stroke-width="2" stroke-dasharray="4 3"/><circle cx="46" cy="46" r="36" fill="#fff" stroke="#ccc"/><path d="M36 30c-4 4-2 14 6 22s18 10 22 6l-6-7-5 3c-4-2-8-6-10-10l3-5z" fill="#6ba51c"/></svg>
  <h3>PHONE CALLS</h3><p>Lorem Ipsum is simply dummy text of the printing and typesetting industry.</p>
</div>
<div class="abs card" style="left:754px;top:900px">
  <svg class="card-badge" viewBox="0 0 92 92"><circle cx="46" cy="46" r="44" fill="#fff" stroke="#6ba51c" stroke-width="2" stroke-dasharray="4 3"/><circle cx="46" cy="46" r="36" fill="#fff" stroke="#ccc"/><rect x="34" y="32" width="20" height="26" fill="none" stroke="#6ba51c" stroke-width="3"/><rect x="40" y="27" width="20" height="26" fill="#fff" stroke="#6ba51c" stroke-width="3"/><path d="M44 35h12M44 40h12M44 45h12" stroke="#6ba51c" stroke-width="2"/></svg>
  <h3>TEXT MESSAGES</h3><p>Lorem Ipsum is simply dummy text of the printing and typesetting industry.</p>
</div>
<div class="abs card" style="left:197px;top:1115px">
  <svg class="card-badge" viewBox="0 0 92 92"><circle cx="46" cy="46" r="44" fill="#fff" stroke="#6ba51c" stroke-width="2" stroke-dasharray="4 3"/><circle cx="46" cy="46" r="36" fill="#fff" stroke="#ccc"/><rect x="30" y="34" width="32" height="22" fill="#6ba51c"/><path d="M30 34l16 13 16-13" stroke="#fff" stroke-width="2" fill="none"/></svg>
  <h3>EMAIL</h3><p>Lorem Ipsum is simply dummy text of the printing and typesetting industry.</p>
</div>
<div class="abs card" style="left:474px;top:1115px">
  <svg class="card-badge" viewBox="0 0 92 92"><circle cx="46" cy="46" r="44" fill="#fff" stroke="#6ba51c" stroke-width="2" stroke-dasharray="4 3"/><circle cx="46" cy="46" r="36" fill="#fff" stroke="#ccc"/><rect x="32" y="32" width="26" height="26" fill="none" stroke="#6ba51c" stroke-width="3"/><path d="M37 44l7 7 14-16" stroke="#6ba51c" stroke-width="4" fill="none"/></svg>
  <h3>BANNER ADS</h3><p>Lorem Ipsum is simply dummy text of the printing and typesetting industry.</p>
</div>
<div class="abs card" style="left:754px;top:1115px">
  <svg class="card-badge" viewBox="0 0 92 92"><circle cx="46" cy="46" r="44" fill="#fff" stroke="#6ba51c" stroke-width="2" stroke-dasharray="4 3"/><circle cx="46" cy="46" r="36" fill="#fff" stroke="#ccc"/><path d="M34 58l6-16 14-12 8 8-12 14z" fill="#6ba51c"/><path d="M34 58l10-10" stroke="#fff" stroke-width="2"/></svg>
  <h3>BLOGS</h3><p>Lorem Ipsum is simply dummy text of the printing and typesetting industry.</p>
</div>

<!-- partners -->
<section class="abs partners"></section>
<h2 class="abs section-title" style="top:1393px">Our Reputed Merchants</h2>
<svg class="abs carousel-arrow" style="left:149px;top:1495px" viewBox="0 0 20 36"><path d="M16 3 4 18l12 15" fill="none" stroke="#666" stroke-width="5"/></svg>
<div class="abs pbox" style="left:183px;top:1470px">ticketvane</div>
<div class="abs pbox" style="left:401px;top:1470px">skarn</div>
<div class="abs pbox" style="left:618px;top:1470px">vortel</div>
<div class="abs pbox" style="left:834px;top:1470px">Brynmor</div>
<svg class="abs carousel-arrow" style="left:1032px;top:1495px" viewBox="0 0 20 36"><path d="M4 3l12 15L4 33" fill="none" stroke="#666" stroke-width="5"/></svg>

<h2 class="abs section-title" style="top:1595px">Our Reputed Affilates</h2>
<svg class="abs carousel-arrow" style="left:149px;top:1696px" viewBox="0 0 20 36"><path d="M16 3 4 18l12 15" fill="none" stroke="#666" stroke-width="5"/></svg>
<div class="abs pbox" style="left:183px;top:1671px">Danube Bistro</div>
<div class="abs pbox" style="left:401px;top:1671px">Forge Labs</div>
<div class="abs pbox" style="left:618px;top:1671px">Pilot Fin Assoc</div>
<div class="abs pbox" style="left:834px;top:1671px">Pulse Depot</div>
<svg class="abs carousel-arrow" style="left:1032px;top:1696px" viewBox="0 0 20 36"><path d="M4 3l12 15L4 33" fill="none" stroke="#666" stroke-width="5"/></svg>

<!-- testimonials -->
<h2 class="abs section-title" style="top:1870px">Thousands of Online Business Love us!</h2>
<article class="abs testimonial" style="overflow:hidden">
  <div class="abs quote-mark" style="left:22px;top:20px">&ldquo;</div>
  <p class="abs t-text" style="left:20px;top:54px;width:270px">Lorem Ipsum has been the industry's standard dummy text ever since the 1500s, when an unknown printer took a galley of type and scrambled it to make a type specimen book.</p>
  <div class="abs t-photo" role="img" aria-label="Portrait photo of the reviewer"></div>
  <p class="abs t-text" style="left:20px;top:136px;width:360px">Lorem Ipsum has been the industry's standard dummy text ever since the 1500s, when an unknown printer took a galley of type and scrambled it to make a type specimen book. It has survived not only five centuries, but also the leap into electronic typesetting, remaining essentially unchanged. It was popularised in the 1960s with the release of Letraset sheets containing Lorem Ipsum passages, and more recently with desktop publishing software like Aldus PageMaker including versions of Lorem Ipsum. <a class="more" href="#">read more</a></p>
  <div class="abs t-deco">&rdquo;</div>
  <div class="abs t-name" style="left:20px;top:288px">Colin Marsh</div>
  <div class="abs t-role" style="left:20px;top:310px">Product Manager, Brightvale Systems</div>
</article>

<div class="abs client" style="left:607px;top:1943px;width:111px;height:66px;font-size:13px">Helix Ventures</div>
<div class="abs client" style="left:733px;top:1943px;width:144px;height:66px;font-size:16px">trailgrip.com</div>
<div class="abs client" style="left:892px;top:1943px;width:125px;height:66px;font-size:14px">Ridgeway</div>
<div class="abs client" style="left:607px;top:2022px;width:111px;height:66px;font-size:15px">Q-Post</div>
<div class="abs client" style="left:733px;top:2022px;width:208px;height:66px;font-size:20px">audiotale fest</div>
<div class="abs client" style="left:955px;top:2022px;width:62px;height:66px;font-size:10px">Kestrel</div>
<div class="abs client" style="left:607px;top:2102px;width:111px;height:68px;font-size:12px">Sherwood Orient</div>
<div class="abs client" style="left:733px;top:2102px;width:208px;height:68px;font-size:17px">Eastmark Contracting</div>
<div class="abs client" style="left:955px;top:2102px;width:62px;height:68px;font-size:10px">Flarex</div>
<div class="abs client" style="left:607px;top:2183px;width:111px;height:111px;font-size:13px">Greyridge Apparel</div>
<div class="abs client" style="left:733px;top:2183px;width:284px;height:111px;font-size:30px">Snackbox</div>
<div class="abs t-dots"><span></span><span></span><span></span></div>

<!-- footer -->
<footer class="abs footer"></footer>
<div class="abs f-head" style="left:185px;top:2404px;width:448px">About Us</div>
<p class="abs f-text" style="left:185px;top:2452px;width:448px">Lorem Ipsum is simply dummy text of the printing and typesetting industry. Lorem Ipsum has been the industry's standard dummy text ever since the 1500s, when an unknown printer took a galley of type and scrambled it to make a type specimen book. It has survived not only five centuries, but also the leap into electronic typesetting, remaining essentially unchanged. It was popularised in the 1960s with the release of Letraset sheets containing Lorem Ipsum passages, and more recently with desktop publishing software like Aldus PageMaker including versions of Lorem Ipsum.</p>

<div class="abs f-head" style="left:185px;top:2592px;width:140px">Get Started</div>
<div class="abs f-links" style="left:185px;top:2638px">How It Works<br>Our Pricing<br>Why Us?</div>
<div class="abs f-head" style="left:338px;top:2592px;width:140px">Help</div>
<div class="abs f-links" style="left:338px;top:2638px">FAQ's<br>Payout Tips<br>Contact us</div>
<div class="abs f-head" style="left:491px;top:2592px;width:142px">Company</div>
<div class="abs f-links" style="left:491px;top:2638px">About Us<br>Services<br>Blog Posts</div>

<div class="abs f-head" style="left:722px;top:2404px;width:298px">Get in Touch</div>
<div class="abs f-phone" style="left:722px;top:2446px">0000 000 0000</div>
<div class="abs f-mail" style="left:722px;top:2478px">help@maplecourtlink.com</div>
<div class="abs f-note"><p>Lorem Ipsum is simply dummy text of the printing and typesetting industry.</p><p style="margin-top:12px">Lorem Ipsum is simply dummy text of the printing and typesetting industry.</p></div>
<svg class="abs" style="left:740px;top:2626px" width="22" height="16" viewBox="0 0 22 16"><path d="M0 0h22L4 16z" fill="#6ba51c"/></svg>
<a class="abs social" style="left:719px;top:2671px" href="#">Lumo</a>
<a class="abs social" style="left:777px;top:2671px" href="#">Trillo</a>
<a class="abs social" style="left:836px;top:2671px" href="#">Nexa</a>
<a class="abs social" style="left:893px;top:2671px" href="#">Orbi</a>

<div class="abs f-brand"><i></i>Maple Court Link</div>
<div class="abs copyright">2014 Maple Court Link.com. - All Rights Reserved</div>

</body>
</html>
```